Business card for new business - financial management

I need a business card designed for my new business. I'm the owner / sole trader of TVH Consulting, which provides financial management services for Government. I'd like the design to incorporate the attached business name and colours. The design should include colour and not be too way out - it needs to look at home in a government environment.
Details to be included on the card are:
TVH Consulting
Delia Ravick
0400 938 214
deliaeravick@mailbrook.net
47 Pellham Crescent, Marlowe ACT 2614
Single or double sided designs would be good.
Target Market(s)
Employees at Australian Federal Government agencies
Industry/Entity Type
Government
Look and feel

```html
<!DOCTYPE html>
<html lang="en">
<head>
<meta charset="utf-8">
<title>TVH Consulting – Business Card</title>
<link rel="stylesheet" href="https://fonts.googleapis.com/css2?family=Lato:wght@400;700&display=swap">
<style>
  :root {
    --bg: #e9ecee;
    --card: #ffffff;
    --teal-dark: #1e5968;
    --teal-light: #6d9fae;
    --name: #1f5b6d;
    --ink: #1d2326;
    --muted: #6a6f73;
  }
  * { box-sizing: border-box; margin: 0; padding: 0; }
  html, body {
    width: 1200px; height: 1116px; overflow: hidden;
    background: var(--bg);
    font-family: "Lato", Arial, sans-serif;
  }
  .card {
    position: absolute; left: 100px; top: 272px;
    width: 1000px; height: 572px;
    background: var(--card);
    box-shadow: 0 12px 40px rgba(0,0,0,.18);
    overflow: hidden;
  }
  .brand {
    position: absolute; left: 200px; top: 150px;
    font-size: 62px; font-weight: 400; color: var(--teal-dark);
    letter-spacing: .5px; white-space: nowrap;
  }
  .holder {
    position: absolute; left: 640px; top: 268px;
  }
  .holder-name {
    font-size: 34px; font-weight: 700; color: var(--name);
    white-space: nowrap;
  }
  .holder-role {
    margin-top: 4px; font-size: 17px; font-weight: 700;
    color: var(--ink); letter-spacing: .4px; white-space: nowrap;
  }
  .contacts {
    position: absolute; left: 84px; top: 352px;
    list-style: none;
  }
  .contact {
    display: flex; align-items: center; gap: 14px;
    height: 40px;
    font-size: 19px; color: var(--muted); white-space: nowrap;
  }
  .contact svg { width: 22px; height: 22px; fill: var(--teal-dark); flex: none; }
  .band { position: absolute; left: 0; bottom: 0; width: 1000px; height: 110px; }
</style>
</head>
<body>
  <div class="card">
    <div class="brand">TVH Consulting</div>

    <div class="holder">
      <div class="holder-name">Delia Ravick</div>
      <div class="holder-role">OWNER / SOLE TRADER</div>
    </div>

    <ul class="contacts">
      <li class="contact">
        <svg viewBox="0 0 24 24" aria-hidden="true"><path d="M6.6 10.8a15.1 15.1 0 0 0 6.6 6.6l2.2-2.2a1 1 0 0 1 1-.25 11.4 11.4 0 0 0 3.6.57 1 1 0 0 1 1 1V20a1 1 0 0 1-1 1A17 17 0 0 1 3 4a1 1 0 0 1 1-1h3.5a1 1 0 0 1 1 1c0 1.25.2 2.45.57 3.57a1 1 0 0 1-.25 1z"/></svg>
        <span>0400 938 214</span>
      </li>
      <li class="contact">
        <svg viewBox="0 0 24 24" aria-hidden="true"><path d="M2 5h20v14H2zm2 2v.3l8 5.6 8-5.6V7zm0 2.7V17h16V9.7l-8 5.6z"/></svg>
        <span>deliaeravick@mailbrook.net</span>
      </li>
      <li class="contact">
        <svg viewBox="0 0 24 24" aria-hidden="true"><path d="M12 2a7 7 0 0 0-7 7c0 5.2 7 13 7 13s7-7.8 7-13a7 7 0 0 0-7-7zm0 9.5A2.5 2.5 0 1 1 12 6.5a2.5 2.5 0 0 1 0 5z"/></svg>
        <span>47 Pellham Crescent, Marlowe ACT 2614</span>
      </li>
    </ul>

    <svg class="band" viewBox="0 0 1000 110" preserveAspectRatio="none" aria-hidden="true">
      <path d="M600 66 Q612 36 646 34 L1000 34 L1000 66 Z" fill="var(--teal-light)"/>
      <path d="M0 92 L600 68 L1000 68 L1000 110 L0 110 Z" fill="var(--teal-dark)"/>
    </svg>
  </div>
</body>
</html>
```